Clean, Fresh Business Card Design Needed

We need a business card design for a new business we have taken over called "Bonders and Fillers". We got a logo through this website which i have attached. We are wanting something that is vibrant but clean and fresh. Our business mainly sells glue. Maybe a cool design/slogan on the back? Modern, sleek.

Industry/Entity Type

Business

Contact Information for Business Card

Name: Ewan Tressider, Managing Director. Address: 164 Kelmond Road, Tauranga 3117, Phone: 07 462 3947 Mobile: 021 354 921 Fax: 07 462 5086 Email: bondfill.mail@pelorix.co.nz, Web: www.stickwarex.co.nz

Font styles to use
Serif

Requirements
Must have
• All business card details, logo.
Nice to have
• Design, slogan on back of card

```html
<!DOCTYPE html>
<html lang="en">
<head>
<meta charset="utf-8">
<title>Bonders and Fillers – Business Card</title>
<link rel="stylesheet" href="https://fonts.googleapis.com/css2?family=Cinzel:wght@400&family=Open+Sans:wght@400;700&display=swap">
<style>
  :root {
    --navy: #2f2d6b;
    --navy-deep: #24225a;
    --navy-soft: #3d3b80;
    --paper: #ffffff;
    --backdrop: #e4e4e6;
    --ink: #1f1f24;
    --ink-muted: #444450;
  }
  * { margin: 0; padding: 0; box-sizing: border-box; }
  html, body {
    width: 1200px; height: 726px; overflow: hidden;
    background: var(--backdrop);
  }
  .canvas { position: relative; width: 1200px; height: 726px; }
  .card {
    position: absolute; top: 213px;
    width: 525px; height: 300px;
    overflow: hidden;
    box-shadow: 0 6px 18px rgba(0,0,0,0.18);
  }
  .card--front { left: 60px; background: var(--navy); }
  .card--back  { left: 615px; background: var(--paper); }

  /* Decorative splash areas (flat stand-ins) */
  .splash { position: absolute; }
  .card--front .splash {
    right: 0; top: 0; width: 215px; height: 300px;
    background: linear-gradient(135deg, #f4f4f8 0%, #d9d9e6 100%);
    border-radius: 0 0 0 140px;
  }
  .card--back .splash {
    left: 0; bottom: 0; width: 210px; height: 220px;
    background: linear-gradient(135deg, var(--navy-soft) 0%, var(--navy-deep) 100%);
    border-radius: 0 140px 0 0;
  }

  /* Wordmark */
  .wordmark { position: absolute; display: flex; align-items: center; gap: 12px; }
  .wordmark__square { width: 34px; height: 34px; flex: none; }
  .wordmark__name {
    font-family: "Cinzel", serif; font-weight: 400;
    line-height: 1.05; letter-spacing: 1px;
  }
  .card--front .wordmark {
    left: 64px; top: 96px;
    flex-direction: column; align-items: flex-start; gap: 10px;
  }
  .card--front .wordmark__square { width: 44px; height: 44px; background: var(--paper); margin-left: 4px; }
  .card--front .wordmark__name { color: var(--paper); font-size: 28px; }

  .card--back .wordmark { left: 220px; top: 36px; }
  .card--back .wordmark__square { background: var(--navy); }
  .card--back .wordmark__name { color: var(--navy); font-size: 21px; white-space: nowrap; }

  /* Contact block */
  .contact {
    position: absolute; left: 240px; top: 112px;
    font-family: "Open Sans", sans-serif; color: var(--ink);
  }
  .contact__name { font-weight: 700; font-size: 14px; }
  .contact__role { font-size: 10px; color: var(--ink-muted); margin-bottom: 14px; }
  .contact__list { list-style: none; font-size: 12px; line-height: 1.7; }
  .contact__row { display: flex; align-items: center; gap: 6px; white-space: nowrap; }
  .contact__row .gap { width: 10px; }
  .icon { width: 11px; height: 11px; flex: none; fill: var(--navy); }
</style>
</head>
<body>
<main class="canvas">

  <section class="card card--front" aria-label="Card front">
    <div class="splash" role="img" aria-label="Large white glue splash graphic"></div>
    <div class="wordmark">
      <span class="wordmark__square"></span>
      <span class="wordmark__name">Bonders<br>and Fillers</span>
    </div>
  </section>

  <section class="card card--back" aria-label="Card back">
    <div class="splash" role="img" aria-label="Large navy glue splash graphic"></div>
    <div class="wordmark">
      <span class="wordmark__square"></span>
      <span class="wordmark__name">Bonders and Fillers</span>
    </div>

    <div class="contact">
      <p class="contact__name">Ewan Tressider</p>
      <p class="contact__role">Manager</p>
      <ul class="contact__list">
        <li class="contact__row">
          <svg class="icon" viewBox="0 0 12 12" aria-label="Mobile"><rect x="3" y="0.5" width="6" height="11" rx="1"/><rect x="4" y="2" width="4" height="7" fill="#fff"/></svg>
          <span>021 354 921</span>
          <span class="gap"></span>
          <svg class="icon" viewBox="0 0 12 12" aria-label="Fax"><rect x="3" y="0.5" width="6" height="4" fill="none" stroke="#2f2d6b"/><rect x="0.5" y="4" width="11" height="6" rx="1"/><rect x="3" y="8" width="6" height="3.5" fill="#fff" stroke="#2f2d6b"/></svg>
          <span>07 462 5086</span>
        </li>
        <li class="contact__row">
          <svg class="icon" viewBox="0 0 12 12" aria-label="Phone"><path d="M1 4 Q6 -1 11 4 L9 5.5 L8 4 Q6 3 4 4 L3 5.5 Z"/><rect x="2.5" y="6" width="7" height="5" rx="1"/></svg>
          <span>07 462 3947</span>
        </li>
        <li class="contact__row">
          <svg class="icon" viewBox="0 0 12 12" aria-label="Email"><rect x="0.5" y="2" width="11" height="8"/><path d="M0.5 2 L6 7 L11.5 2" fill="none" stroke="#fff"/></svg>
          <span>bondfill.mail@pelorix.co.nz</span>
        </li>
        <li class="contact__row">
          <svg class="icon" viewBox="0 0 12 12" aria-label="Web"><circle cx="6" cy="6" r="5.5"/><path d="M0.5 6 H11.5 M6 0.5 V11.5" stroke="#fff" fill="none"/></svg>
          <span>www.stickwarex.co.nz</span>
        </li>
        <li class="contact__row">
          <svg class="icon" viewBox="0 0 12 12" aria-label="Address"><path d="M6 0.5 A4 4 0 0 1 10 4.5 C10 7 6 11.5 6 11.5 C6 11.5 2 7 2 4.5 A4 4 0 0 1 6 0.5 Z"/><circle cx="6" cy="4.5" r="1.5" fill="#fff"/></svg>
          <span>164 Kelmond Road, Tauranga 3117</span>
        </li>
      </ul>
    </div>
  </section>

</main>
</body>
</html>
```